Limousine Service Company Website

we need a website designed for a Meridian Limousine company with global capabilities (meaning they can service clients throughout the US and the world)

They service mostly corporate/business travelers, and groups and meetings, with a small portion of their business devoted to retail clients (special events and personal travel)

The overall look should be corporate, and we prefer a responsive design. We will need a home page, a fleet page (examples can be seen here: https://www.brovalecars.com/fleet
http://www.pennowayrides.com/our-fleet) and one interior page

Copy will be lorem epsum for now

We have no logo yet but can put a placeholder logo

```html
<!DOCTYPE html>
<html lang="en">
<head>
<meta charset="utf-8">
<title>Meridian Limousine – Home</title>
<link rel="stylesheet" href="https://fonts.googleapis.com/css2?family=Arimo:wght@400;700&family=Open+Sans:wght@400;600&display=swap">
<style>
:root{
  --page:#f7f7f7;
  --white:#ffffff;
  --blue:#0a6eb8;
  --blue-dark:#075a98;
  --ink:#222222;
  --text:#555555;
  --muted:#666666;
  --orange:#f08a1c;
  --hero-orange:#f5a21b;
  --icon-grey:#e2e2e2;
  --rule:#e4e4e4;
}
*{margin:0;padding:0;box-sizing:border-box}
html,body{width:966px;height:1200px;overflow:hidden;background:var(--page)}
body{position:relative;font-family:"Open Sans",Arial,sans-serif;color:var(--text)}
.abs{position:absolute}

/* header */
.brand{left:8px;top:11px;width:278px;height:120px;background:var(--white);display:flex;align-items:center;gap:10px;padding-left:22px}
.brand-dot{width:16px;height:16px;border-radius:50%;background:var(--ink)}
.brand-name{font-family:"Arimo",Arial,sans-serif;font-size:25px;line-height:1.05;color:var(--ink);font-weight:400}
.phone-box{left:787px;top:60px;width:120px;height:36px;background:var(--white)}
.phone{left:792px;top:95px;width:140px;height:41px;background:var(--white);display:flex;align-items:center;gap:8px;padding-left:6px;font-family:"Arimo",Arial,sans-serif;font-size:11.5px;color:var(--muted)}

/* nav */
.nav{left:0;top:153px;width:966px;height:46px;background:var(--blue);border-bottom:1px solid #5596c8}
.nav ul{list-style:none;display:flex;padding-left:20px;height:100%}
.nav li{height:100%;display:flex;align-items:center;justify-content:center;font-family:"Arimo",Arial,sans-serif;font-size:12px;color:var(--white);border-right:1px solid var(--blue-dark)}
.nav li.active{background:var(--blue);color:var(--ink);border-bottom:4px solid var(--ink);padding-top:4px}

/* hero */
.hero{left:0;top:199px;width:966px;height:403px;background:linear-gradient(180deg,#6d6b63 0%,#b9b7b2 28%,#dcdcdc 55%,#e9e9ea 80%,#cfcfd1 100%);border-bottom:1px solid var(--orange)}
.hero-caption{left:113px;top:224px;width:740px;height:109px;background:rgba(20,20,20,.72);padding:7px 23px;font-family:"Open Sans",Arial,sans-serif;font-size:19.5px;line-height:32px;color:var(--hero-orange)}
.slider-arrows{left:448px;top:618px;display:flex;gap:11px}
.slider-arrows span{width:29px;height:29px;border-radius:50%;border:1px solid #cfd6dc;background:var(--white);display:flex;align-items:center;justify-content:center}

/* features */
.feature{top:688px;height:214px;text-align:center}
.feature + .feature{border-left:1px solid var(--rule)}
.feature h2{font-family:"Arimo",Arial,sans-serif;font-weight:400;font-size:22px;color:var(--blue);letter-spacing:.3px;margin-top:3px}
.feature svg{display:block;margin:12px auto 0}
.feature p{text-align:justify;font-size:10.4px;line-height:19.3px;letter-spacing:.2px;margin:24px 0 0;color:var(--text)}
.more{display:inline-block;vertical-align:middle;margin-left:6px}

/* lower */
.lower{left:0;top:952px;width:966px;height:248px;border-top:1px solid var(--rule)}
.section-title{font-family:"Arimo",Arial,sans-serif;font-weight:400;font-size:22px;color:var(--blue);letter-spacing:.3px}
.copy{font-size:10.4px;line-height:19.3px;text-align:justify;letter-spacing:.1px}
.copy.lead{color:var(--orange)}
.event-rule{border:0;border-top:1px solid var(--rule);margin:14px 0 16px}
.car-photo{border-radius:4px}
</style>
</head>
<body>

<header>
  <div class="abs brand">
    <span class="brand-dot"></span>
    <span class="brand-name">Meridian<br>Limo Service</span>
  </div>
  <div class="abs phone-box"></div>
  <div class="abs phone">
    <svg width="14" height="18" viewBox="0 0 14 18" aria-hidden="true"><path d="M3 1 L6 1 L7 5 L5 6.5 Q6 10 8.5 12.5 L10 11 L13 13 L12.5 16 Q6 17 2.5 10 Q0.5 5 3 1Z" fill="#777"/></svg>
    (100) 555-01234
  </div>
</header>

<nav class="abs nav">
  <ul>
    <li class="active" style="width:91px">HOME</li>
    <li style="width:91px">FLEET</li>
    <li style="width:91px">INTERIOR</li>
    <li style="width:90px;border-right:0">CONTACTS</li>
  </ul>
</nav>

<section class="abs hero" role="img" aria-label="White stretch limousine parked on a snowy road in front of a white chapel"></section>
<p class="abs hero-caption">At Meridian Limousine, we use our experience, commitment and focus on quality, to provide the finest chauffeured ground transportation services throughout the world</p>

<div class="abs slider-arrows">
  <span><svg width="18" height="12" viewBox="0 0 18 12" aria-hidden="true"><path d="M0 6 L7 0 V4 H18 V8 H7 V12Z" fill="var(--blue)"/></svg></span>
  <span><svg width="18" height="12" viewBox="0 0 18 12" aria-hidden="true"><path d="M18 6 L11 0 V4 H0 V8 H11 V12Z" fill="var(--blue)"/></svg></span>
</div>

<section class="abs feature" style="left:40px;width:260px">
  <h2>FAST &amp; SAFE</h2>
  <svg width="76" height="76" viewBox="0 0 76 76" aria-hidden="true"><circle cx="38" cy="38" r="33" fill="none" stroke="var(--icon-grey)" stroke-width="9"/><path d="M36 18 V42 H54" fill="none" stroke="var(--icon-grey)" stroke-width="8"/></svg>
  <p>Lorem ipsum dolor sit amet conse ctetur adipisic-ing elit, sed do eiusmod tempor incididunt ut labore et dolore magna aliqua. Ut enim ad minim veniam, quis nostrud.<svg class="more" width="18" height="18" viewBox="0 0 18 18" aria-hidden="true"><circle cx="9" cy="9" r="9" fill="var(--blue)"/><path d="M14 9 L9.5 5 V7.5 H4 V10.5 H9.5 V13Z" fill="#fff"/></svg></p>
</section>

<section class="abs feature" style="left:322px;width:318px;padding:0 28px 0 30px">
  <h2>BEST PRICES</h2>
  <svg width="70" height="76" viewBox="0 0 70 76" aria-hidden="true"><path d="M6 34 H18 V72 H6Z" fill="var(--icon-grey)"/><path d="M22 34 L36 6 Q44 4 44 14 L40 28 H62 Q68 30 66 38 L60 68 Q58 72 52 72 H22Z" fill="none" stroke="var(--icon-grey)" stroke-width="7" stroke-linejoin="round"/></svg>
  <p>Lorem ipsum dolor sit amet conse ctetur adipisic-ing elit, sed do eiusmod tempor incididunt ut labore et dolore magna aliqua. Ut enim ad minim veniam, quis nostrud.<svg class="more" width="18" height="18" viewBox="0 0 18 18" aria-hidden="true"><circle cx="9" cy="9" r="9" fill="var(--blue)"/><path d="M14 9 L9.5 5 V7.5 H4 V10.5 H9.5 V13Z" fill="#fff"/></svg></p>
</section>

<section class="abs feature" style="left:640px;width:326px;padding:0 38px 0 28px">
  <h2>RENTAL SERVICE</h2>
  <svg width="80" height="72" viewBox="0 0 80 72" aria-hidden="true"><path d="M27 12 V5 Q27 2 30 2 H50 Q53 2 53 5 V12" fill="none" stroke="var(--icon-grey)" stroke-width="5"/><rect x="2" y="12" width="76" height="58" rx="6" fill="var(--icon-grey)"/><rect x="15" y="12" width="4" height="58" fill="var(--page)"/><rect x="61" y="12" width="4" height="58" fill="var(--page)"/></svg>
  <p>Lorem ipsum dolor sit amet conse ctetur adipisic-ing elit, sed do eiusmod tempor incididunt ut labore et dolore magna aliqua. Ut enim ad minim veniam, quis nostrud.<svg class="more" width="18" height="18" viewBox="0 0 18 18" aria-hidden="true"><circle cx="9" cy="9" r="9" fill="var(--blue)"/><path d="M14 9 L9.5 5 V7.5 H4 V10.5 H9.5 V13Z" fill="#fff"/></svg></p>
</section>

<div class="abs lower"></div>

<section class="abs" style="left:40px;top:970px;width:267px">
  <h2 class="section-title">ABOUT</h2>
  <p class="copy" style="margin-top:14px">Lorem ipsum dolor sit amet conse ctetur adipisicing elit, sed do eiusmod tempor incididunt ut labore et dolore magna aliqua.</p>
  <p class="copy" style="margin-top:14px">Ut enim ad minim veniam, quis nostrud exercitation ullamco laboris nisi ut aliquip ex ea commodo conse-quat. Duis aute irure dolor in reprehenderit in voluptate velit esse cillum dolore eu fugiat nulla pariatur. Excepteur sint occaecat cupidatat non proident, sunt in culpa qui officia deserunt mollit</p>
</section>

<section class="abs" style="left:336px;top:970px;width:266px">
  <h2 class="section-title">OUR EVENTS</h2>
  <p class="copy lead" style="margin-top:14px">Lorem ipsum dolor sit amet conse ctetur adipisicing elit, sed do eiusmod tempor</p>
  <p class="copy" style="margin-top:18px">Ut enim ad minim veniam, quis nostrud exercitation ullamco laboris nisi ut aliquip ex ea commodo conse-quat. Duis aute irure dolor.</p>
  <hr class="event-rule">
  <p class="copy lead">Lorem ipsum dolor sit amet conse ctetur adipisicing</p>
</section>

<div class="abs car-photo" style="left:628px;top:974px;width:298px;height:72px;background:linear-gradient(180deg,#f7f7f7 0%,#3a3a3c 30%,#151515 70%,#e8e8e8 100%)" role="img" aria-label="Black stretch limousine, side view"></div>
<div class="abs car-photo" style="left:628px;top:1079px;width:298px;height:116px;background:linear-gradient(180deg,#f7f7f7 0%,#dedfe1 25%,#f2f2f2 55%,#9a9a9c 85%,#eeeeee 100%)" role="img" aria-label="White stretch limousine, front three-quarter view"></div>

</body>
</html>
```